Succession & Estate Planning firm needs a double-sided one page client handout

We need a client hand-out that highlights the top 10 Reasons to get a Pension Plan. It will need the 10 reasons as headings, with a short description of each reason (attached Word doc). It should communicate that a Pension Plan is flexible and provides security. Our usual client is a business owner/medical professional/entrepreneur. Have a look at our website for more info about our business www.quorvane.ca Our logo colours are 83c242, 3b3839, d5d5d5 We like clean, modern, info-graphics, not too cluttered, not too loudWe would like the ability to update the text/content ourselves, in the future.

```html
<!DOCTYPE html>
<html lang="en">
<head>
<meta charset="utf-8">
<title>Top 10 Reasons – Why an FPP Serves Your Family Enterprise</title>
<link href="https://fonts.googleapis.com/css2?family=Arimo:wght@400;700&family=Montserrat:wght@400;500;600&display=swap" rel="stylesheet">
<style>
  :root {
    --brand-green: #83c242;
    --brand-green-light: #a9d873;
    --brand-charcoal: #3b3839;
    --brand-grey: #d5d5d5;
    --paper: #f4f5f3;
    --paper-shade: #e6e8e5;
    --backdrop: #dcdcd8;
    --body-text: #2c2a2b;
  }
  * { box-sizing: border-box; margin: 0; padding: 0; }
  html, body { width: 1200px; height: 1200px; overflow: hidden; }
  body {
    background: var(--backdrop);
    font-family: "Arimo", Arial, sans-serif;
    color: var(--body-text);
    position: relative;
  }
  .handout {
    position: absolute;
    top: 200px;
    width: 540px;
    height: 800px;
    background: linear-gradient(180deg, #fbfbfa 0%, var(--paper) 55%, var(--paper-shade) 100%);
    box-shadow: 0 6px 22px rgba(0,0,0,.18);
    overflow: hidden;
  }
  .handout--front { left: 40px; }
  .handout--back { left: 620px; }

  .tree-art {
    position: absolute;
    top: 0; right: 0;
    width: 330px; height: 260px;
    background: radial-gradient(ellipse at 60% 30%, rgba(131,194,66,.40) 0%, rgba(169,216,115,.22) 45%, rgba(244,245,243,0) 72%);
  }
  .leaf-art {
    position: absolute;
    top: 0; left: 0;
    width: 300px; height: 160px;
    background: radial-gradient(ellipse at 30% 30%, rgba(131,194,66,.22) 0%, rgba(244,245,243,0) 70%);
  }
  .grass-art {
    position: absolute;
    left: 0; right: 0; bottom: 0;
    height: 46px;
    background: linear-gradient(180deg, rgba(131,194,66,0) 0%, rgba(131,194,66,.75) 55%, #6aa92f 100%);
  }

  .brand {
    position: absolute;
    top: 60px; left: 38px;
    display: flex; align-items: center; gap: 10px;
  }
  .brand__name {
    font-family: "Montserrat", Arial, sans-serif;
    font-weight: 400;
    font-size: 30px;
    letter-spacing: 5px;
    color: var(--brand-charcoal);
    text-transform: uppercase;
  }
  .brand__dot {
    width: 14px; height: 14px; border-radius: 50%;
    background: var(--brand-green);
  }

  .title-pill {
    position: absolute;
    top: 130px; left: 26px;
    width: 470px;
    padding: 16px 28px 18px;
    border-radius: 40px;
    background: var(--brand-green);
    color: #fff;
    font-family: "Montserrat", Arial, sans-serif;
  }
  .title-pill__main { font-size: 32px; font-weight: 600; line-height: 1.1; }
  .title-pill__sub { font-size: 17px; font-weight: 500; margin-top: 4px; white-space: nowrap; }

  .reasons { position: absolute; left: 26px; right: 30px; }
  .handout--front .reasons { top: 270px; }
  .handout--back .reasons { top: 40px; }

  .reason { margin-bottom: 24px; }
  .reason__head { display: flex; align-items: center; position: relative; }
  .reason__num {
    flex: none;
    width: 44px; height: 44px; border-radius: 50%;
    background: #fff;
    border: 3px solid var(--brand-green);
    display: flex; align-items: center; justify-content: center;
    font-family: "Arimo", Arial, sans-serif;
    font-weight: 700; font-size: 17px;
    color: var(--brand-charcoal);
    position: relative; z-index: 1;
  }
  .reason__title {
    margin-left: -18px;
    padding: 7px 20px 7px 28px;
    border-radius: 0 22px 22px 0;
    background: var(--brand-green);
    color: #fff;
    font-family: "Montserrat", Arial, sans-serif;
    font-weight: 500;
    font-size: 15px;
    letter-spacing: .2px;
    text-transform: uppercase;
    white-space: nowrap;
  }
  .reason__text {
    margin-top: 8px;
    padding-left: 6px;
    font-size: 12.5px;
    line-height: 1.38;
    text-align: justify;
  }
</style>
</head>
<body>

<section class="handout handout--front" aria-label="Handout front">
  <div class="tree-art" role="img" aria-label="Soft illustration of a leafy green tree"></div>
  <div class="grass-art" role="img" aria-label="Strip of green grass"></div>

  <div class="brand">
    <span class="brand__name">Quorvane</span>
    <span class="brand__dot"></span>
  </div>

  <div class="title-pill">
    <div class="title-pill__main">Top 10 Reasons</div>
    <div class="title-pill__sub">Why an FPP Serves Your Family Enterprise</div>
  </div>

  <div class="reasons">
    <article class="reason">
      <div class="reason__head"><span class="reason__num">01</span><h2 class="reason__title">Create Significant Deductions</h2></div>
      <p class="reason__text">The FPP creates significant tax deductions, which can be used to keep the business under the small business rate or applied to the high rate, a bigger bang for the buck.</p>
    </article>
    <article class="reason">
      <div class="reason__head"><span class="reason__num">02</span><h2 class="reason__title">Deliberate, Planned, Future</h2></div>
      <p class="reason__text">An income for beyond the last day at the office.</p>
    </article>
    <article class="reason">
      <div class="reason__head"><span class="reason__num">03</span><h2 class="reason__title">Past Buy Back</h2></div>
      <p class="reason__text">Most owners invest, first, in the business. The FPP offers the ability to go back and recover lost years when they did not buy RRSPs…and pass the tax savings onto their company.</p>
    </article>
    <article class="reason">
      <div class="reason__head"><span class="reason__num">04</span><h2 class="reason__title">Creditor Proof</h2></div>
      <p class="reason__text">All Assets held in an FPP are creditor proof, including RRSPs, and planned pension contributions receive “super-priority” status, which rank above the claims of secured creditors, like major commercial lenders and banks.</p>
    </article>
  </div>
</section>

<section class="handout handout--back" aria-label="Handout back">
  <div class="leaf-art" role="img" aria-label="Faint green leaves"></div>
  <div class="grass-art" role="img" aria-label="Strip of green grass"></div>

  <div class="reasons">
    <article class="reason">
      <div class="reason__head"><span class="reason__num">05</span><h2 class="reason__title">Flexibility</h2></div>
      <p class="reason__text">Owners know that cash flows can swing wildly with the business cycle. An FPP offers the flexibility to flip between DB and DC accounts in order to conserve cash, smooth income during volatile years, and recover assets when things improve.</p>
    </article>
    <article class="reason">
      <div class="reason__head"><span class="reason__num">06</span><h2 class="reason__title">Preserve the Lifetime Capital Gains Exemption</h2></div>
      <p class="reason__text">Create $1.6 Million++ of Tax Free Capital Gains. The significant deductions created in an FPP can be used to purify a corporation with passive assets, which can help preserve the shareholders’ lifetime capital gains exemption.</p>
    </article>
    <article class="reason">
      <div class="reason__head"><span class="reason__num">07</span><h2 class="reason__title">Intergenerational Wealth Transfer</h2></div>
      <p class="reason__text">Unlike RRSPs that eventually trigger a taxable disposition upon death, an FPP has the ability to pass, tax deferred, to the next generation of family business owners.</p>
    </article>
    <article class="reason">
      <div class="reason__head"><span class="reason__num">08</span><h2 class="reason__title">All Ages</h2></div>
      <p class="reason__text">An FPP can benefit all entrepreneurs between ages 18-71.</p>
    </article>
    <article class="reason">
      <div class="reason__head"><span class="reason__num">09</span><h2 class="reason__title">Preserve the Small Business</h2></div>
      <p class="reason__text">Assets inside an FPP grows tax exempt and does not create passive income under the 2018 “Halvorsen Measures”. Therefore, business owners can use these sources to fund their pension assets will not jeopardize their small business deduction on active profits and in associated companies.</p>
    </article>
    <article class="reason">
      <div class="reason__head"><span class="reason__num">10</span><h2 class="reason__title">Broader Investment Options</h2></div>
      <p class="reason__text">An FPP allows entrepreneurs to invest in what they like: real estate, other businesses and/or franchises, private equity, public equity, exempt markets, etc. The possibilities are up to the imagination of the entrepreneur and their advisors.</p>
    </article>
  </div>
</section>

</body>
</html>
```